Life Coach for Lawyers Business Card Design

Elegant, original, business card design for life coaching service for associate attorneys who work in big law and struggle with stress, overwhelm, and time management. Double sided design.

Target Market(s)

Women associate attorneys who work in big law and struggle with stress, overwhelm, and time management.

Industry/Entity Type

Life Coaching

Contact Information for Business Card

Marissa Pendrell
Life Coach
518.677.3941
calmbriefcounsel.net
marissa@calmbriefcounsel.net
@calmbriefcounsel (Instagram)

Font styles to use
Other font styles liked:
• Silver South font duo. See uploaded files.

Requirements
Must have
• Icons for phone, website, email, and Instagram instead of words. Specific colors used in my logo (171B2B, 421121, FFFFFF)
Nice to have
• Foil. Embossed. Feminine design.
Should not have
• Any colors other than those used in logo. See uploaded files.

```html
<!DOCTYPE html>
<html lang="en">
<head>
<meta charset="UTF-8">
<title>Calm Brief Counsel – Business Card</title>
<link rel="stylesheet" href="https://fonts.googleapis.com/css2?family=Roboto:wght@400;500;700&display=swap">
<style>
  :root {
    --ink-navy: #171B2B;
    --wine: #421121;
    --paper: #FFFFFF;
    --stage: #E4E4E4;
    --muted: #555860;
  }
  * { margin: 0; padding: 0; box-sizing: border-box; }
  html, body {
    width: 1125px;
    height: 1200px;
    overflow: hidden;
    background: var(--stage);
    font-family: "Roboto", Arial, sans-serif;
  }
  .card {
    position: absolute;
    left: 171px;
    width: 826px;
    height: 471px;
    background: var(--paper);
    text-align: center;
  }
  .card--front {
    top: 106px;
    display: flex;
    align-items: center;
    justify-content: center;
  }
  .card--back { top: 639px; }

  .contact-block {
    display: flex;
    flex-direction: column;
    align-items: center;
  }
  .contact-block__name {
    font-size: 29px;
    font-weight: 700;
    color: var(--wine);
    letter-spacing: 0.5px;
    line-height: 34px;
    text-transform: uppercase;
  }
  .contact-block__role {
    font-size: 20px;
    font-weight: 500;
    color: var(--ink-navy);
    letter-spacing: 0.4px;
    line-height: 26px;
    text-transform: uppercase;
  }
  .contact-list {
    list-style: none;
    margin-top: 14px;
    display: flex;
    flex-direction: column;
    align-items: flex-start;
    gap: 2px;
  }
  .contact-list__item {
    display: flex;
    align-items: center;
    gap: 10px;
    font-size: 19px;
    font-weight: 400;
    color: var(--muted);
    line-height: 26px;
    white-space: nowrap;
  }
  .contact-list__icon {
    width: 17px;
    height: 17px;
    flex: none;
    fill: none;
    stroke: var(--wine);
    stroke-width: 1.8;
    stroke-linecap: round;
    stroke-linejoin: round;
  }
  .contact-list__dot {
    width: 13px;
    height: 13px;
    margin: 0 2px;
    flex: none;
    border-radius: 50%;
    background: var(--wine);
  }

  .brand-name {
    position: absolute;
    left: 0;
    right: 0;
    top: 50%;
    transform: translateY(-50%);
    font-size: 54px;
    font-weight: 500;
    color: var(--wine);
    letter-spacing: 2px;
    text-transform: uppercase;
  }
</style>
</head>
<body>
  <section class="card card--front">
    <div class="contact-block">
      <p class="contact-block__name">Marissa Pendrell</p>
      <p class="contact-block__role">Life Coach</p>
      <ul class="contact-list">
        <li class="contact-list__item">
          <svg class="contact-list__icon" viewBox="0 0 24 24" aria-label="Phone"><path d="M5 3h4l2 5-2.5 1.5a11 11 0 0 0 6 6L16 13l5 2v4a2 2 0 0 1-2 2A16 16 0 0 1 3 5a2 2 0 0 1 2-2z"/></svg>
          <span>518.677.3941</span>
        </li>
        <li class="contact-list__item">
          <svg class="contact-list__icon" viewBox="0 0 24 24" aria-label="Email"><rect x="3" y="5" width="18" height="14" rx="2"/><path d="M3 7l9 6 9-6"/></svg>
          <span>marissa@calmbriefcounsel.net</span>
        </li>
        <li class="contact-list__item">
          <svg class="contact-list__icon" viewBox="0 0 24 24" aria-label="Website"><circle cx="12" cy="12" r="9"/><path d="M3 12h18M12 3c3 3 3 15 0 18M12 3c-3 3-3 15 0 18"/></svg>
          <span>calmbriefcounsel.net</span>
        </li>
        <li class="contact-list__item">
          <span class="contact-list__dot" aria-label="Social profile"></span>
          <span>@calmbriefcounsel</span>
        </li>
      </ul>
    </div>
  </section>

  <section class="card card--back">
    <p class="brand-name">Calm Brief Counsel</p>
  </section>
</body>
</html>
```